2017 Massachusetts Patrol Deputy Statute Digest Cover

Each year I put out a new Patrol Deputy Statute Digest. I'm looking for a new design for 2017. I like to change the look each year. I've included the last couple of years versions as samples along with my logos. I like the 2016 version much better than the 2016. Incorporating an actual image is a plus. The book is also geared specifically to Massachusetts Police Officers.

Target Market(s)

Massachusetts Police officers

Font styles to use
Serif
Other font styles liked:
• designer choice

Requirements
Must have
• Eye popping design that is professional and not too flashy. Back cover and spine is also needed.
Nice to have
• Photo image(s)
Should not have
• Copyright protected images or images that identify a specific police agency as I would require their permission.

```html
<!DOCTYPE html>
<html lang="en">
<head>
<meta charset="utf-8">
<title>Patrol Deputy Statute Digest 2017 – Cover</title>
<link rel="stylesheet" href="https://fonts.googleapis.com/css2?family=Marcellus&family=EB+Garamond:ital,wght@0,400;0,500;1,400;1,500&display=swap">
<style>
  :root {
    --navy: #1e2550;
    --maroon: #7a2e26;
    --gold: #9a7a35;
    --gold-light: #c9a24a;
    --ink: #1f1f2a;
    --paper: #f4f2ef;
    --mist: #dfe3ec;
  }
  * { margin: 0; padding: 0; box-sizing: border-box; }
  html, body { width: 1200px; height: 702px; overflow: hidden; background: var(--paper); }
  .cover {
    position: relative; width: 1200px; height: 702px; overflow: hidden;
    background: linear-gradient(90deg, #e9ecf2 0%, #f3f3f4 45%, #f6f5f3 100%);
    font-family: "EB Garamond", Georgia, serif; color: var(--ink);
  }

  /* Back cover */
  .back-photo {
    position: absolute; left: 0; top: 0; width: 560px; height: 702px;
    background:
      radial-gradient(ellipse at 10% 90%, rgba(120,110,100,.35), transparent 45%),
      radial-gradient(ellipse at 15% 8%, rgba(110,125,160,.45), transparent 40%),
      linear-gradient(180deg, rgba(200,206,220,.6), rgba(240,240,242,.3) 60%, rgba(170,170,180,.45));
  }
  .back-emblem {
    position: absolute; left: 246px; top: 50px; width: 44px; height: 60px;
    background: linear-gradient(180deg, #c9a65a, #9a7a35); border-radius: 4px; opacity: .85;
  }
  .back-title {
    position: absolute; left: 56px; top: 126px; width: 430px;
    font-family: "Marcellus", "Times New Roman", serif; font-size: 22px; letter-spacing: .3px;
    color: var(--navy); white-space: nowrap;
  }
  .back-title .accent { color: var(--maroon); margin-left: 6px; }
  .rule { position: absolute; height: 3px; background: var(--gold); }
  .back-rule-top { left: 56px; top: 182px; width: 430px; }
  .back-rule-bottom { left: 56px; top: 549px; width: 430px; }
  .back-blurb {
    position: absolute; left: 56px; top: 202px; width: 430px;
    font-size: 13.2px; line-height: 17.6px; text-align: justify; color: #1c1c28;
  }
  .back-blurb p { text-indent: 8px; }
  .back-blurb p + p.gap { margin-top: 6px; }
  .copyright {
    position: absolute; left: 56px; top: 572px;
    font-style: italic; font-size: 14.5px; line-height: 19px; color: var(--maroon);
  }

  /* Spine */
  .spine-title, .spine-author {
    position: absolute; writing-mode: vertical-rl;
    font-family: "Marcellus", "Times New Roman", serif; white-space: nowrap;
  }
  .spine-title { left: 572px; top: 34px; font-size: 22px; line-height: 24px; }
  .spine-title .line-1 { color: var(--navy); }
  .spine-title .line-2 { color: var(--maroon); }
  .spine-year {
    position: absolute; left: 575px; top: 244px; writing-mode: vertical-rl;
    font-family: "EB Garamond", Georgia, serif; font-size: 38px; color: var(--maroon); letter-spacing: 1px;
  }
  .spine-mark {
    position: absolute; left: 571px; top: 360px; writing-mode: vertical-rl;
    display: flex; align-items: center; gap: 6px;
    font-family: "Marcellus", serif; font-size: 13px; color: var(--gold); letter-spacing: 1px;
  }
  .spine-mark .dot { width: 14px; height: 14px; border-radius: 50%; background: var(--gold); }
  .spine-author { left: 578px; top: 478px; font-size: 15px; line-height: 20px; color: var(--maroon); }

  /* Front cover */
  .front-title {
    position: absolute; left: 640px; top: 22px; width: 560px; text-align: center;
    font-family: "Marcellus", "Times New Roman", serif; line-height: 1;
  }
  .front-title .line-1 { display: block; font-size: 44px; color: var(--navy); letter-spacing: .5px; }
  .front-title .line-2 { display: block; font-size: 52px; color: var(--maroon); margin-top: 10px; letter-spacing: .5px; }
  .front-year {
    position: absolute; left: 640px; top: 138px; width: 560px;
    display: flex; justify-content: center; align-items: center; gap: 12px;
    font-size: 40px; color: var(--gold); line-height: 1;
  }
  .front-year .dash { width: 60px; height: 2px; background: var(--gold); }
  .front-photo {
    position: absolute; left: 658px; top: 194px; width: 542px; height: 338px;
    border-top: 4px solid var(--gold); border-bottom: 4px solid var(--gold);
    background:
      radial-gradient(ellipse at 85% 40%, rgba(210,200,185,.75), transparent 35%),
      radial-gradient(ellipse at 30% 18%, rgba(230,120,50,.55), transparent 25%),
      linear-gradient(180deg, #5b4e45 0%, #8d8a85 35%, #d9d9d6 60%, #6b6f74 100%);
  }
  .front-mark {
    position: absolute; left: 868px; top: 440px;
    display: flex; align-items: center; gap: 8px;
    font-family: "Marcellus", serif; font-size: 20px; color: var(--gold-light); letter-spacing: 1px;
  }
  .front-mark .dot { width: 18px; height: 18px; border-radius: 50%; background: var(--gold-light); }
  .front-guide {
    position: absolute; left: 658px; top: 552px; width: 542px; text-align: center;
    font-family: "Marcellus", serif; font-size: 17px; color: var(--navy); white-space: nowrap;
  }
  .front-guide-rule { left: 722px; top: 575px; width: 416px; height: 2px; }
  .front-topics {
    position: absolute; left: 658px; top: 586px; width: 542px; text-align: center;
    font-style: italic; font-weight: 500; font-size: 19.5px; line-height: 27px; color: var(--navy);
  }
  .front-author {
    position: absolute; left: 658px; top: 652px; width: 542px; text-align: center;
    font-size: 15px; letter-spacing: .3px; color: var(--maroon);
  }
</style>
</head>
<body>
<main class="cover">

  <section class="back-cover">
    <div class="back-photo" role="img" aria-label="Soft-focus photograph of an officer holding handcuffs behind a person's back"></div>
    <div class="back-emblem" role="img" aria-label="Small scales of justice emblem"></div>
    <h2 class="back-title">PATROL DEPUTY'S<span class="accent">STATUTE DIGEST</span></h2>
    <div class="rule back-rule-top"></div>
    <div class="back-blurb">
      <p>Lorem ipsum dolor sit amet, consectetur adipiscing elit. Pellentesque elit felis, porta non risus at, mattis sagittis mauris. Sed risus quam, fermentum ac luctus ac, ullamcorper eleifend dolor. Fusce posuere eu nisl sed auctor. Mauris vel ipsum mauris. Phasellus congue eget sapien non tempus.</p>
      <p>Fusce ut mollis est. Pellentesque ipsum libero, suscipit ut scelerisque aliquet, rhoncus non ligula. Nunc efficitur enim ac nisi mattis, vel varius justo imperdiet. Aliquam bibendum, nisl vitae mattis ultrices, orci tellus sollicitudin neque, sit amet sollicitudin felis metus eget justo.</p>
      <p class="gap">Aliquam et tempus augue. Lorem ipsum dolor sit amet, consectetur adipiscing elit. Etiam lacus odio, tincidunt vitae eleifend ut, sagittis sed odio. Integer consectetur tellus metus, vel ultricies odio congue nec. Sed in eros vitae diam euismod pulvinar.</p>
      <p>Lum sociis natoque penatibus et magnis dis parturient montes, nascetur ridiculus mus. Vestibulum pharetra. Dolor non sem hendrerit, eget ultricies ante dignissim mauris non interdum nisl. Curabitur est libero, placerat id. Lorem ipsum dolor sit amet, consectetur adipiscing elit. Etiam lacus odio, tincidunt vitae eleifend ut, sagittis sed odio.</p>
    </div>
    <div class="rule back-rule-bottom"></div>
    <p class="copyright">© 2017 Whitcombe Training Group, LLC<br>All Rights Reserved</p>
  </section>

  <section class="spine">
    <h2 class="spine-title"><span class="line-1">PATROL DEPUTY'S</span><br><span class="line-2">STATUTE DIGEST</span></h2>
    <div class="spine-year">2017</div>
    <div class="spine-mark"><span class="dot"></span>WHITCOMBE</div>
    <p class="spine-author">LIEUTENANT DANIEL<br>R. WHITCOMBE, ESQ.</p>
  </section>

  <section class="front-cover">
    <h1 class="front-title"><span class="line-1">PATROL DEPUTY'S</span><span class="line-2">STATUTE DIGEST</span></h1>
    <div class="front-year"><span class="dash"></span>2017<span class="dash"></span></div>
    <div class="front-photo" role="img" aria-label="Photograph of a patrol car with roof lights beside a statue of Lady Justice holding scales, on a city street"></div>
    <div class="front-mark"><span class="dot"></span>WHITCOMBE</div>
    <p class="front-guide">MASSACHUSETTS PATROL DEPUTY'S GUIDE TO:</p>
    <div class="rule front-guide-rule"></div>
    <p class="front-topics">Criminal Procedure, Statutory Law,<br>Motor Vehicle Law and Juvenile Law</p>
    <p class="front-author">LIEUTENANT DANIEL R. WHITCOMBE, ESQ.</p>
  </section>

</main>
</body>
</html>
```